Broschüren-Design für Schuhmanufaktur
Zielgruppe
Schuhmanufaktur für Maßschuhe möchte sich modernisieren.
Aufgabenstellung
Maße und andere Daten entnehmen Sie sich den angefügten Daten und Bildern.
Es soll eine Broschüre (Maße etc in daten und skizze) und ein Plakat mit composing erstellt werden.
Offene Daten erwünscht (.ai)

```html
<!DOCTYPE html>
<html lang="de">
<head>
<meta charset="utf-8">
<title>Sohlwerk – 20 Jahre Schuhmanufaktur Plakat</title>
<link href="https://fonts.googleapis.com/css2?family=Quicksand:wght@300;400;500;600;700&display=swap" rel="stylesheet">
<style>
  :root {
    --canvas-bg: #eeeeee;
    --frame: #0d0d0d;
    --photo-dark: #2a1a14;
    --photo-mid: #6b3f2a;
    --photo-warm: #a4613c;
    --photo-light: #c9875a;
    --headline-box: rgba(150, 86, 48, 0.82);
    --tagline-box: rgba(28, 20, 18, 0.78);
    --service-grey: #3b3938;
    --service-brown: #2d1c17;
    --text-light: #ffffff;
    --text-soft: #d9d4d0;
  }
  * { margin: 0; padding: 0; box-sizing: border-box; }
  html, body {
    width: 1200px;
    height: 848px;
    overflow: hidden;
    background: var(--canvas-bg);
    font-family: "Quicksand", sans-serif;
  }
  .canvas {
    position: relative;
    width: 1200px;
    height: 848px;
    display: flex;
    align-items: center;
    justify-content: center;
  }
  .poster {
    width: 548px;
    height: 820px;
    background: var(--frame);
    padding: 13px;
    box-shadow: 0 12px 30px rgba(0,0,0,0.18);
  }
  .poster-inner {
    position: relative;
    width: 522px;
    height: 794px;
    overflow: hidden;
  }
  .hero-photo {
    position: absolute;
    left: 0; top: 0;
    width: 522px;
    height: 636px;
    background:
      radial-gradient(ellipse at 80% 50%, rgba(201,135,90,0.55), transparent 55%),
      radial-gradient(ellipse at 20% 75%, rgba(164,97,60,0.6), transparent 50%),
      radial-gradient(ellipse at 10% 40%, rgba(20,14,12,0.8), transparent 45%),
      linear-gradient(160deg, var(--photo-mid) 0%, var(--photo-warm) 40%, var(--photo-mid) 70%, var(--photo-dark) 100%);
  }
  .brand-name {
    position: absolute;
    top: 150px;
    left: 0; right: 0;
    text-align: center;
    color: var(--text-light);
    font-size: 38px;
    font-weight: 600;
    letter-spacing: 1px;
  }
  .headline {
    position: absolute;
    left: 0; right: 0;
    display: flex;
    justify-content: center;
  }
  .headline span {
    display: inline-block;
    background: var(--headline-box);
    color: var(--text-light);
    font-weight: 600;
    line-height: 1;
  }
  .headline-years { top: 268px; }
  .headline-years span { font-size: 62px; padding: 2px 8px 2px; }
  .headline-trade { top: 345px; }
  .headline-trade span { font-size: 40px; padding: 4px 7px; }
  .headline-brand { top: 402px; }
  .headline-brand span { font-size: 40px; padding: 4px 7px; }
  .tagline {
    position: absolute;
    left: 0; right: 0;
    display: flex;
    justify-content: center;
  }
  .tagline span {
    display: inline-block;
    background: var(--tagline-box);
    color: var(--text-light);
    font-weight: 300;
    font-size: 38px;
    line-height: 1;
    padding: 3px 6px 4px;
  }
  .tagline-one { top: 496px; }
  .tagline-two { top: 551px; }
  .services {
    position: absolute;
    left: 0; bottom: 0;
    width: 522px;
    height: 158px;
    display: flex;
  }
  .service {
    flex: 1;
    background: var(--service-grey);
    text-align: center;
    padding-top: 26px;
    color: var(--text-soft);
  }
  .service--highlight { background: var(--service-brown); }
  .service h2 {
    color: var(--text-light);
    font-size: 19px;
    font-weight: 600;
    margin-bottom: 8px;
  }
  .service p {
    font-size: 15.5px;
    font-weight: 400;
    line-height: 21px;
  }
</style>
</head>
<body>
<main class="canvas">
  <article class="poster">
    <div class="poster-inner">
      <div class="hero-photo" role="img" aria-label="Foto einer Schuhmacherwerkbank mit Lederschuh, Hammer, Zangen und Werkzeugen in warmen Brauntönen"></div>

      <div class="brand-name">Sohlwerk</div>

      <div class="headline headline-years"><span>20 JAHRE</span></div>
      <div class="headline headline-trade"><span>SCHUHMANUFAKTUR</span></div>
      <div class="headline headline-brand"><span>SOHLWERK</span></div>

      <div class="tagline tagline-one"><span>Leder ist unsere</span></div>
      <div class="tagline tagline-two"><span>Leidenschaft</span></div>

      <section class="services">
        <div class="service">
          <h2>REPARATUR</h2>
          <p>Wir ermöglichen<br>hochwertigen<br>Lederwaren lange<br>Nutzbarkeit</p>
        </div>
        <div class="service service--highlight">
          <h2>OPTIMIERUNG</h2>
          <p>Wir übernehmen<br>spezielle<br>Anpassungswünsche</p>
        </div>
        <div class="service">
          <h2>KREATION</h2>
          <p>Wir fertigen<br>individuelle<br>Maßschuhe</p>
        </div>
      </section>
    </div>
  </article>
</main>
</body>
</html>
```